New e-commerce site needs a clean, responsive design with a focus on great UX

Sky Cover is a start-up online firearm parts store, aimed at offering a great shopping experience. We want to differentiate ourselves from other online stores firstly through a clean design that doesn't try to compete with itself for user attention.

This project is for the home page specifically, but further work may include the individual product page, category page, and checkout flow pages.

The design must:
* Be clean and clutter-free, with judicious use of white space.
* Be responsive, in that elements must be able to reflow without problems, such that mobile users retain full functionality.
* Be content-focussed, with header and footer styling taking a backseat to content styling.
* Avoid column-based side bars (Navigation, etc.) as far as possible.
* Avoid carousels, or any other sort of rotating content. We want to avoid animations of any kind, again, to avoid competing with ourselves for user attention.
* Scroll cleanly. Scrolling is fine - we don't care about cramming everything in above The Fold, so long as scrolling cues are available.
* Feature a clean typographical hierarchy to properly direct user attention.
* A clean grid, such that blocks line up nicely, within reason. We understand that text does not always work out in perfect rectangles.

The current placeholder design is viewable at http://www.skycover-demo.co.za/ (Also check it out on a mobile device to see responsive behaviour)

Sites in the same type of industry that have the type of clean look we want:
* http://www.trekmoorvale.com/ (Not ideal, but in the right general direction)
* http://brindle.tolvexgear.com/ (Great-looking content areas and fantastic responsive design)
The content areas are the main focus here, especially on the latter site. We don't want the same type of header or footer styling as these sites, as exemplified by the very Bootstrappy placeholder site we currently have.

Elements we would like to see in the design:
* The slogan with an AC-130 gunship (The current one is a public domain image), which gives context behind the brand name and ties into the silhouette placeholder logo.
* A product spotlight, to highlight a particular product we would like to bring attention to. It need not be as verbose as the "Introducing the Brass Binner" spotlight currently on the placeholder site, but should still be a headline spotlight.
* "Mini" spotlights for specific brands, categories, or specific products. This is sort-of implemented as the "Brands In Stock" section on the placeholder site, but the final design would probably have more squarish blocks, so that a specific product consisting of image and headline could be featured. Feel free to use random product images as needed.

Other notes:
* The use of Courier New for headings is to try convey a "military/air force" feel, but we don't want to go overboard with that, which is why there are no other "military" aspects to the site. Exploration of other options are welcome.
* Please let us know if there's any other information or guidance we can provide to help with the design process.

Edit 2015/01/07 07:40 UTC:
* This contest is for PSD designs, but if you prefer to implement it using HTML & CSS, you are welcome to do so, with Bootstrap being preferred. The requirement to keep in mind is that whatever is in the design must be able to reflow cleanly for lower-resolution devices (Down to 320px wide). In other words, the design must be able to be implemented in a responsive manner.
* We don't strictly require the design to include the AC-130 gunship, but it does help tie the brand name to the slogan and thus anchor the brand name in users' minds. If the same message can be conveyed differently, we're happy to consider it.
* We would prefer to avoid stereotypical "military" elements, such as camouflage, etc.

Edit 2015/01/07 08:08 UTC:
* The design must avoid pop-up menus, or anything that would require pop-up menus.
* Going forward, the plan is to include breadcrumbs just below the header on sub-pages of the site. This breadcrumb section will be full-width, and will be able to expand down to show a category navigation panel. This will push any other body content down. If necessary, we can create mockups of how we envision this to look, so that the design can account for it.

Reason: We'd like to allow designers more time to refine their designs. Based on what we have seen so far, we have switched the project from refundable to committed status.

```html
<!DOCTYPE html>
<html lang="en">
<head>
<meta charset="utf-8">
<title>Sky Cover — Home</title>
<link rel="stylesheet" href="https://fonts.googleapis.com/css2?family=Noto+Sans:wght@400;700&family=Open+Sans:wght@400;600;700&display=swap">
<style>
  :root {
    --red: #c8000a;
    --ink: #3a3a3a;
    --text: #5b5b5b;
    --rule: #dedede;
    --white: #ffffff;
    --hero-dark: #1b1b1b;
    --hero-mid: #383838;
    --footer: #151515;
    --footer-bar: #262626;
    --brand-grey: #9c9c9c;
    --steel-light: #c9cbcd;
    --steel-dark: #6d7073;
  }
  * { box-sizing: border-box; margin: 0; padding: 0; }
  html, body { width: 1012px; height: 1200px; overflow: hidden; background: var(--white); }
  body { font-family: "Open Sans", Arial, sans-serif; color: var(--text); }
  .container { width: 720px; margin: 0 auto; position: relative; }

  /* Header */
  .site-header { height: 47px; }
  .site-header .container { display: flex; align-items: center; justify-content: space-between; height: 47px; }
  .brand { font-family: "Noto Sans", Arial, sans-serif; font-weight: 700; font-size: 13px; color: var(--red); letter-spacing: .2px; padding-left: 60px; }
  .main-nav { display: flex; font-size: 9.5px; font-weight: 600; color: #333; }
  .main-nav a { color: inherit; text-decoration: none; }
  .main-nav span.sep { margin: 0 9px; color: #666; }
  .main-nav .cart { color: var(--red); font-weight: 700; }

  /* Hero */
  .hero { height: 275px; background: radial-gradient(ellipse at 55% 40%, var(--hero-mid), var(--hero-dark) 75%); position: relative; }
  .hero .container { height: 275px; }
  .hero-title { position: absolute; left: -2px; top: 68px; font-family: "Noto Sans", Arial, sans-serif; font-weight: 700; font-size: 35px; color: var(--white); letter-spacing: .5px; line-height: 1; }
  .hero-sub { position: absolute; left: -2px; top: 113px; font-family: "Noto Sans", Arial, sans-serif; font-weight: 700; font-size: 20px; color: #a2a2a2; letter-spacing: .4px; }
  .btn-shop { position: absolute; left: 0; top: 171px; width: 165px; height: 39px; background: var(--red); color: var(--white); font-family: "Noto Sans", Arial, sans-serif; font-weight: 700; font-size: 19px; display: flex; align-items: center; justify-content: center; gap: 12px; text-decoration: none; }
  .hero-visual { position: absolute; left: 380px; top: 36px; width: 330px; height: 200px; border-radius: 20px; background: linear-gradient(120deg, var(--steel-light), var(--steel-dark)); opacity: .55; }

  /* Categories */
  .categories { height: 221px; border-bottom: 1px solid var(--rule); width: 720px; margin: 0 auto; }
  .cat-grid { display: flex; justify-content: space-between; padding-top: 30px; }
  .cat-card { width: 150px; text-align: center; }
  .cat-image { width: 130px; height: 100px; margin: 0 auto; border-radius: 8px; background: linear-gradient(135deg, #e4e5e7, #a8abae); }
  .cat-card h3 { font-family: "Noto Sans", Arial, sans-serif; font-weight: 700; font-size: 14.5px; color: var(--ink); margin-top: 24px; }

  /* Spotlight */
  .spotlight { height: 345px; border-bottom: 1px solid var(--rule); width: 720px; margin: 0 auto; position: relative; }
  .spotlight-image { position: absolute; left: 2px; top: 55px; width: 335px; height: 225px; border-radius: 110px; background: linear-gradient(100deg, #2f53c8 0%, #e7d23a 45%, #2a2a2a 100%); }
  .spotlight-copy { position: absolute; left: 372px; top: 40px; width: 340px; }
  .spotlight-copy h2 { font-family: "Noto Sans", Arial, sans-serif; font-weight: 700; font-size: 36px; color: var(--ink); letter-spacing: 1px; line-height: 1; }
  .spotlight-copy h3 { font-family: "Noto Sans", Arial, sans-serif; font-weight: 700; font-size: 24px; color: var(--red); margin-top: 4px; letter-spacing: .3px; line-height: 1.2; }
  .spotlight-copy p { font-size: 10.5px; line-height: 19px; margin-top: 10px; }
  .spotlight-copy p + p { margin-top: 17px; }
  .btn-read { display: inline-flex; align-items: center; gap: 9px; margin-top: 13px; width: 100px; height: 27px; justify-content: center; background: var(--red); color: var(--white); font-family: "Noto Sans", Arial, sans-serif; font-weight: 700; font-size: 10px; text-decoration: none; }

  /* Brands */
  .brands { height: 108px; width: 720px; margin: 0 auto; display: flex; align-items: center; justify-content: space-between; padding-bottom: 6px; }
  .brand-name { font-family: "Noto Sans", Arial, sans-serif; font-weight: 700; font-size: 19px; color: var(--brand-grey); }

  /* Footer */
  .site-footer { border-top: 4px solid var(--red); background: var(--footer); height: 147px; }
  .footer-grid { display: flex; padding-top: 28px; }
  .footer-col { padding-left: 11px; }
  .footer-col:nth-child(1) { width: 183px; }
  .footer-col:nth-child(2) { width: 201px; }
  .footer-col:nth-child(3) { width: 182px; }
  .footer-col h4 { font-family: "Noto Sans", Arial, sans-serif; font-weight: 700; font-size: 11px; color: var(--white); margin-bottom: 12px; }
  .footer-col li { list-style: none; font-size: 9px; color: #e2e2e2; line-height: 20px; }
  .footer-col li.accent { color: var(--red); font-weight: 700; font-size: 10px; }
  .footer-bar { background: var(--footer-bar); height: 67px; text-align: center; font-size: 8.5px; color: #8f8f8f; padding-top: 16px; }
</style>
</head>
<body>
  <header class="site-header">
    <div class="container">
      <div class="brand">SKY COVER</div>
      <nav class="main-nav">
        <a href="#">PRODUCTS</a><span class="sep">|</span>
        <a href="#">OUR BRANDS</a><span class="sep">|</span>
        <a href="#">FIND A DEALER</a><span class="sep">|</span>
        <a href="#">CONTACT</a><span class="sep">|</span>
        <a href="#">WISH LIST</a><span class="sep">|</span>
        <a href="#">MY ACCOUNT</a><span class="sep">|</span>
        <a href="#" class="cart">CART: 0</a>
      </nav>
    </div>
  </header>

  <section class="hero">
    <div class="container">
      <h1 class="hero-title">SED PERSPICIATIS</h1>
      <div class="hero-sub">ERROR SIT VOLUPTATEM</div>
      <a href="#" class="btn-shop">SHOP NOW <span>›</span></a>
      <div class="hero-visual" role="img" aria-label="Three steel reloading dies on a dark background"></div>
    </div>
  </section>

  <section class="categories">
    <div class="cat-grid">
      <div class="cat-card"><div class="cat-image" role="img" aria-label="Set of reloading dies"></div><h3>Lorem Ipsum</h3></div>
      <div class="cat-card"><div class="cat-image" role="img" aria-label="Steel bolt part"></div><h3>Lorem Ipsum</h3></div>
      <div class="cat-card"><div class="cat-image" role="img" aria-label="Trigger and spring parts kit"></div><h3>Lorem Ipsum</h3></div>
      <div class="cat-card"><div class="cat-image" role="img" aria-label="Three roll pins"></div><h3>Lorem Ipsum</h3></div>
    </div>
  </section>

  <section class="spotlight">
    <div class="spotlight-image" role="img" aria-label="Blue, yellow and black sorting bowls filled with brass casings"></div>
    <div class="spotlight-copy">
      <h2>INTRODUCING</h2>
      <h3>THE BRASS BINNER</h3>
      <p>Sed ut perspiciatis unde omnis iste natus error sit voluptatem accusantium doloremque laudantium, totam rem aperiam, eaque ipsa quae ab illo inventore veritatis et quasi architecto beatae vitae dicta sunt explicabo.</p>
      <p>Nemo enim ipsam voluptatem quia voluptas sit aspernatur aut odit aut fugit, sed quia consequuntur magni dolores eos qui ratione voluptatem sequi nesciunt.</p>
      <a href="#" class="btn-read">READ MORE <span>›</span></a>
    </div>
  </section>

  <section class="brands">
    <span class="brand-name">Kovari Works</span>
    <span class="brand-name">RIDGEFORD ARMS</span>
    <span class="brand-name">EDGEWRIGHT</span>
    <span class="brand-name">Calloway</span>
  </section>

  <footer class="site-footer">
    <div class="container">
      <div class="footer-grid">
        <div class="footer-col"><h4>HELP</h4><ul><li>Shipping Options</li><li>Payment Options</li><li>FAQ</li></ul></div>
        <div class="footer-col"><h4>MY ACCOUNT</h4><ul><li>Track Order</li><li>Order History</li><li>Preferences</li></ul></div>
        <div class="footer-col"><h4>SKY COVER</h4><ul><li>About</li><li>Coming Soon</li></ul></div>
        <div class="footer-col"><h4>CONTACT US</h4><ul><li>48 Kestrel Lane, Midrand North</li><li class="accent">071 555 0148</li><li class="accent">info@skycover-demo.co.za</li></ul></div>
      </div>
    </div>
  </footer>
  <div class="footer-bar">© 2015 Sky Cover. All Rights Reserved</div>
</body>
</html>
```